Tallowmoor Letterheads Design

Hello, we have just upgraded this project for a guaranteed payment.

We are currently going through a re-branding exercise internally. Our logo is attached as a PDF file.

We are happy with our logo but would like to investigate how we can best apply the logo to our letterheads and compliment slips.

We are a quality printing company in England. Despite our name we are very professional and offer a personal service.

Our new website is under construction and here is a link to show you how it looks: http://brackenpress.v4ntor.co.uk

The style must be professional and steer away from "tacky" otherwise it makes our company look very low budget and just a bit silly.

We would like to see elements of creativity though, so please, nothing too boring.

I have attached our new logo, there is an option for use on white or black.

Cheers
Tallowmoor Team

Reason: We have increased the deadline due to an internal delay to things, we now have more time before we need anything to be printed.

Industry/Entity Type

Construction

Requirements
Must have
• IMPORTANT! Please do not tweak or change our logo in any way. A few designs show vast changes in the logo, this is not what we require. Please do not change the logo in any way. Thanks
Nice to have
• Classy but approachable. Elements of "quirky" would be nice to see.
Should not have
• A Tacky feel

```html
<!DOCTYPE html>
<html lang="en">
<head>
<meta charset="utf-8">
<title>Tallowmoor Letterheads</title>
<link rel="stylesheet" href="https://fonts.googleapis.com/css2?family=Carlito:wght@400;700&family=Arimo:wght@700&display=swap">
<style>
  :root {
    --backdrop: #c9c2c0;
    --paper: #f1f1f0;
    --navy: #13222f;
    --pink: #e0266f;
    --ink: #3a3a3a;
    --white: #ffffff;
    --sky: #9cc3d8;
  }
  * { box-sizing: border-box; margin: 0; padding: 0; }
  html, body { width: 1200px; height: 900px; overflow: hidden; }
  body {
    background: var(--backdrop);
    position: relative;
    font-family: "Carlito", "Calibri", sans-serif;
  }
  .sheet {
    position: absolute;
    top: 93px;
    width: 504px;
    height: 712px;
    background: var(--paper);
  }
  .sheet--back { left: 80px; }
  .sheet--front { left: 615px; }

  .flock-pattern {
    position: absolute;
    inset: 0;
    background:
      radial-gradient(circle at 30% 35%, rgba(224,38,111,0.18), transparent 45%),
      radial-gradient(circle at 70% 65%, rgba(156,195,216,0.25), transparent 45%),
      radial-gradient(circle at 50% 85%, rgba(19,34,47,0.10), transparent 50%),
      var(--paper);
  }

  .masthead {
    height: 95px;
    background: var(--navy);
    position: relative;
    color: var(--white);
  }
  .brand {
    position: absolute;
    left: 17px;
    top: 20px;
    display: flex;
    flex-direction: column;
    align-items: flex-start;
  }
  .brand-row { display: flex; align-items: center; gap: 6px; }
  .brand-dot {
    width: 20px; height: 20px; border-radius: 50%;
    background: var(--pink);
  }
  .brand-name {
    font-family: "Carlito", "Calibri", sans-serif;
    font-size: 24px;
    font-weight: 400;
    color: var(--white);
    letter-spacing: 0.2px;
  }
  .brand-tagline {
    font-size: 8px;
    margin-left: 40px;
    margin-top: -1px;
    color: var(--white);
  }
  .contact {
    position: absolute;
    right: 16px;
    top: 18px;
    text-align: right;
    font-family: "Arimo", "Arial", sans-serif;
    font-weight: 700;
    font-size: 6.6px;
    line-height: 9.3px;
    font-style: normal;
  }
  .contact .gap { margin-top: 9px; }

  .letter {
    position: absolute;
    left: 36px;
    top: 140px;
    width: 430px;
    font-size: 10.2px;
    line-height: 13.1px;
    color: var(--ink);
  }
  .letter p { margin-bottom: 13px; }
  .letter .meta { margin-bottom: 13px; }
  .letter .signoff { margin-top: 33px; }
</style>
</head>
<body>
  <section class="sheet sheet--back">
    <div class="flock-pattern" role="img" aria-label="Scattered pattern of small pink, navy and pale blue sheep illustrations across the back of the letterhead"></div>
  </section>

  <section class="sheet sheet--front">
    <header class="masthead">
      <div class="brand">
        <div class="brand-row">
          <span class="brand-dot"></span>
          <span class="brand-name">Tallowmoor</span>
        </div>
        <span class="brand-tagline">Quality Printing</span>
      </div>
      <address class="contact">
        <div>17 Mill Lane</div>
        <div>Ashcombe-Under-Hill</div>
        <div>Ashcombe, Kent</div>
        <div>TN9 4QE</div>
        <div class="gap">+44 (203) 555-0187</div>
        <div class="gap">www.brackenpress.v4ntor.co.uk</div>
      </address>
    </header>

    <article class="letter">
      <div class="meta">
        To: Clara Dunmore<br>
        Subject: Order status<br>
        Date: 08.10.2013
      </div>
      <p>Dear Ms. Clara Dunmore,</p>
      <p>Lorem ipsum dolor sit amet, netus et malesuada fames ac turpis egestas. Vestibulum tortor quam, feugiat vitae, ultricies eget, tempor sit amet, ante. Donec eu libero sit amet quam egestas semper. Aenean ultricies mi vitae est. Mauris placerat eleifend leo. Quisque sit amet est et sapien ullamcorper pharetra. Vestibulum erat wisi, condimentum sed, commodo vitae, ornare sit amet, wisi. Aenean fermentum, elit eget tincidunt condimentum, eros ipsum rutrum orci, sagittis tempus lacus enim ac dui. Donec non enim in turpis pulvinar facilisis. Ut felis.</p>
      <p>Pellentesque habitant morbi tristique senectus et netus et malesuada fames ac turpis egestas. Vestibulum tortor quam, feugiat vitae, ultricies eget, tempor sit amet, ante. Donec eu libero sit amet quam egestas semper. Aenean ultricies mi vitae est. Mauris placerat eleifend leo.</p>
      <p>Nulla a enim massa. Proin semper, neque vitae laoreet volutpat, dolor elit dapibus urna, id pulvinar lectus dui vitae ligula. Aliquam sed porta diam. Cum sociis natoque penatibus et magnis dis parturient montes, nascetur ridiculus mus. Vestibulum ante ipsum primis in faucibus orci luctus et ultrices posuere cubilia Curae; Cras ullamcorper ipsum sed nunc scelerisque sceleris-que.</p>
      <p>Suspendisse sodales quam eget nulla elementum pretium. Vivamus consectetur luctus dui sit amet ultrices. Sed sed magna porta erat laoreet condimentum. Maecenas sollicitudin commodo massa nec blandit. Aliquam rhoncus magna nec elit placerat commodo. Aenean non ipsum sit amet dolor lacinia blandit. Nam condimentum odio faucibus tellus vestibulum et convallis enim consectetur. Etiam lacinia ornare orci aliquam pretium.</p>
      <div class="signoff">
        Best regards,<br>
        Helen R. Voss
      </div>
    </article>
  </section>
</body>
</html>
```